Senior Care and Care home flyer

We are getting ready to advertise with a company called "DealNest" and our advertisement includes a 3"x8" DOUBLE SIDED insert. Live Area: This is the maximum size of your page content. (Coupon: 3" x 7.9167")
Both sides should have
Address: 4870 Makani Ave. Suite 310 Honolulu, HI 96817
Phone: 808-732-1958
Website: www.BrennerCare.com
-We would like a space for a QR code on both sides

1 side : make color scheme that blue from the last one
Brenner Care Group: featuring Brenner Senior Living
Logo for Senior Living
Brenner Care Group can provide care to your loved ones in our home-Brenner Senior Living Kailua. Clients and their families can experience Brenner's culture of heart-centered, compassionate care in their own home... or in ours.
Senior Living Benefits/Features:
19 Fully Furnished Suites
Meals, Laundry, Housekeeping
Activities & Transportation
On-site 24/7 Care Services
Some items to include on flyer.
Schedule Tour today

Side 2: make the color scheme that green from the last flyer
Brenner Care Group: Featuring Brenner Homecare
Logo for HomeCare
General information for Brenner Care group:
Brenner Care Group has been providing homecare to Oahu's Kupuna for the past 26 years. Brenner Homecare offers personal care services to meet your loved one's needs in the comfort and safety of their own home.
Homecare Services:
Home Health Aides
Skilled Nursing
Bath & Meal Service
Medication Management
Services Available 24/7

Target Market for Side 2: Ages 55-105 Males and Females, looking for care or a home for themselves or their loved ones
-Complimentary Care Consultation
Maybe homecare side says in your home and senior living side said or ours.
Include on both sides
-25+ Years in business
-Locally owned and operated
-Licensed and Insured

Flyer should be 3"x8" DOUBLE SIDED horizontal/landscape/please utilize information that you have used on past ads as a guide.

Industry/Entity Type

Home Health Care Senior Living

Colors
0094D4
00A9DD
6FCCEA
C7EBF8
E9F6FB
00AB8E
00BBA5
67D7C9
C6EFE9
E9F9F6

Requirements
Must have
• Live Area: This is the maximum size of your page content. (Coupon: 3" x 7.9167")
Should not have
• NO PINK OR PEACH colors

```html
<!DOCTYPE html>
<html lang="en">
<head>
<meta charset="utf-8">
<title>Brenner Care Group – Insert</title>
<link href="https://fonts.googleapis.com/css2?family=Roboto:wght@300;400;500;700&family=Poppins:wght@400;500&display=swap" rel="stylesheet">
<style>
  :root{
    --page:#c8c8c8;
    --paper:#ffffff;
    --ink:#222222;
    --ink-soft:#3a3a3a;
    --blue:#0094D4;
    --blue-mid:#00A9DD;
    --blue-soft:#6FCCEA;
    --blue-pale:#C7EBF8;
    --blue-mist:#E9F6FB;
    --green:#00AB8E;
    --green-mid:#00BBA5;
    --green-soft:#67D7C9;
    --green-pale:#C6EFE9;
    --green-mist:#E9F9F6;
  }
  *{box-sizing:border-box;margin:0;padding:0}
  html,body{width:693px;height:1200px;overflow:hidden}
  body{background:var(--page);position:relative;font-family:'Roboto',sans-serif;color:var(--ink)}
  .card{position:absolute;left:26px;width:640px;height:240px;background:var(--paper);overflow:hidden;box-shadow:0 3px 8px rgba(0,0,0,.35)}
  .card--living{top:330px;--accent:var(--blue);--accent-mid:var(--blue-mid);--accent-soft:var(--blue-soft);--accent-pale:var(--blue-pale);--accent-mist:var(--blue-mist)}
  .card--homecare{top:600px;--accent:var(--green);--accent-mid:var(--green-mid);--accent-soft:var(--green-soft);--accent-pale:var(--green-pale);--accent-mist:var(--green-mist)}
  .abs{position:absolute}
  .photo-main{position:absolute;left:0;top:0;width:380px;height:240px}
  .photo-main--living{background:linear-gradient(90deg,#cfd8de 0%,#8aa4b4 38%,#6f8fa3 62%,rgba(255,255,255,0) 100%)}
  .photo-main--homecare{background:linear-gradient(90deg,#a9b5b1 0%,#dfe6e4 35%,#8fa8a2 62%,rgba(255,255,255,0) 100%)}
  .shape{position:absolute;left:0;top:0;width:640px;height:240px}
  .shape .arc{fill:var(--paper);stroke:var(--accent);stroke-width:4}
  .shape .cover{fill:var(--paper)}
  .thumb{position:absolute;border-radius:50%;border:2.5px solid var(--accent)}
  .logo{position:absolute;display:flex;align-items:center;gap:3px;background:var(--paper);padding:4px 5px}
  .logo-mark{width:7px;height:7px;border-radius:50%;background:var(--accent)}
  .logo-name{font-family:'Roboto',sans-serif;font-weight:400;font-size:12px;color:var(--accent)}
  .heading-light{font-weight:300;font-size:18px;line-height:19px;color:var(--ink);letter-spacing:.3px}
  .heading-bold{font-weight:700;font-size:19px;line-height:20px;color:var(--accent)}
  .body-copy{font-size:7.3px;line-height:9.3px;color:var(--ink-soft)}
  .label{font-family:'Poppins',sans-serif;font-size:7.3px;line-height:9px;color:var(--ink)}
  .label--bold{font-family:'Roboto',sans-serif;font-weight:500;font-size:7.5px;line-height:9.3px;color:var(--ink)}
  .divider{position:absolute;width:1px;background:var(--accent)}
  .dot{position:absolute;width:7px;height:7px;border-radius:50%;border:1.5px solid var(--accent-soft);background:radial-gradient(circle,var(--accent) 0 45%,transparent 50%)}
  .panel{position:absolute;background:var(--accent-pale)}
  .icon{position:absolute;width:25px;height:25px;border-radius:50%;background:var(--paper);border:2px solid var(--accent-pale);box-shadow:0 0 0 1.5px var(--accent);display:flex;align-items:center;justify-content:center}
  .icon svg{width:11px;height:11px}
  .feature{position:absolute;text-align:center;font-family:'Poppins',sans-serif;font-size:7.3px;line-height:9px;color:var(--ink)}
  .feature--left{text-align:left}
  .contact{position:absolute;font-family:'Poppins',sans-serif;font-size:7.3px;line-height:10px;color:var(--ink);display:flex;align-items:center;gap:4px}
  .contact svg{width:7px;height:7px}
  .address{position:absolute;font-family:'Poppins',sans-serif;font-size:7.3px;line-height:9.6px;color:var(--ink)}
  .pin{position:absolute;width:8px;height:11px}
  .qr-space{position:absolute;width:30px;height:30px;border:1.2px dashed var(--accent);background:var(--accent-mist)}
  .target{font-weight:500;font-size:7.3px;line-height:9.3px;color:var(--accent)}
  .band-item{position:absolute;display:flex;align-items:flex-start;gap:4px;font-weight:500;font-size:7.5px;line-height:9.3px;color:var(--ink)}
  .band-item::before{content:"";flex:none;width:4px;height:4px;margin-top:3px;border-radius:50%;background:var(--ink);box-shadow:0 0 0 1.5px var(--paper)}
  .band-divider{position:absolute;width:1px;background:var(--paper);top:145px;height:36px}
  .title-right{font-size:17px;line-height:19px;letter-spacing:.2px}
  .title-right .light{font-weight:300;color:var(--ink)}
  .title-right .bold{font-weight:700;color:var(--accent)}
</style>
</head>
<body>

<section class="card card--living">
  <div class="photo-main photo-main--living" role="img" aria-label="Photo of a caregiver and a senior woman chatting on a sofa"></div>
  <svg class="shape" viewBox="0 0 640 240" aria-hidden="true">
    <circle class="arc" cx="110" cy="300" r="250"/>
    <rect class="cover" x="358" y="0" width="282" height="240"/>
  </svg>
  <div class="thumb" style="left:283px;top:16px;width:58px;height:58px;background:radial-gradient(circle,#b9c7cf,#71889a)" role="img" aria-label="Photo of hands holding in comfort"></div>
  <div class="thumb" style="left:313px;top:59px;width:46px;height:46px;background:radial-gradient(circle,#d6e2e8,#7f9aab)" role="img" aria-label="Photo of a furnished suite bedroom"></div>

  <div class="logo" style="left:14px;top:16px">
    <span class="logo-mark"></span><span class="logo-name">Brenner</span>
  </div>

  <div class="abs heading-light" style="left:12px;top:91px">ABOUT</div>
  <div class="abs heading-bold" style="left:13px;top:111px">BRENNER CARE<br>GROUP</div>

  <p class="abs body-copy" style="left:11px;top:174px;width:172px">Brenner Care Group can provide care to your loved ones in our home-Brenner Senior Living Kailua. Clients and their families can experience Brenner's culture of heart-centered, compassionate care in their own home... or in ours.</p>

  <div class="divider" style="left:190px;top:176px;height:46px"></div>
  <span class="dot" style="left:201px;top:182px"></span>
  <div class="abs label--bold" style="left:213px;top:180px">25+ Years in<br>business</div>
  <span class="dot" style="left:267px;top:181px"></span>
  <div class="abs label--bold" style="left:280px;top:179px">Locally owned<br>and operated</div>
  <span class="dot" style="left:201px;top:207px"></span>
  <div class="abs label--bold" style="left:213px;top:205px">Licensed and<br>Insured</div>

  <div class="abs title-right" style="left:379px;top:10px">
    <span class="light">SENIOR LIVING</span> <span class="bold">BENEFITS</span><br><span class="bold">&amp; FEATURES</span>
  </div>

  <div class="panel" style="left:362px;top:59px;width:278px;height:127px;border-radius:63px 0 0 63px"></div>

  <div class="icon" style="left:410px;top:66px"><svg viewBox="0 0 12 12"><rect x="3" y="2" width="6" height="8" rx="1" fill="#222"/></svg></div>
  <div class="feature feature--left" style="left:394px;top:98px">19 Fully Furnished<br>Suites</div>
  <div class="icon" style="left:503px;top:66px"><svg viewBox="0 0 12 12"><circle cx="6" cy="6" r="4.5" fill="none" stroke="#222" stroke-width="1.2"/><path d="M6 3.5V6l1.8 1" stroke="#222" stroke-width="1.1" fill="none"/></svg></div>
  <div class="feature feature--left" style="left:487px;top:98px">On-site 24/7<br>Care Services</div>
  <div class="icon" style="left:576px;top:66px"><svg viewBox="0 0 12 12"><rect x="2.5" y="1.5" width="7" height="9" rx="1" fill="#222"/><circle cx="6" cy="6.5" r="2" fill="#fff"/></svg></div>
  <div class="feature" style="left:561px;top:103px;width:54px">Laundry</div>

  <div class="icon" style="left:410px;top:128px"><svg viewBox="0 0 12 12"><rect x="2" y="2" width="3.5" height="3.5" fill="#222"/><rect x="6.5" y="6.5" width="3.5" height="3.5" fill="#222"/><path d="M5.5 4h3v2" stroke="#222" fill="none"/></svg></div>
  <div class="feature feature--left" style="left:394px;top:159px">Activities &amp;<br>Transportation</div>
  <div class="icon" style="left:503px;top:128px"><svg viewBox="0 0 12 12"><path d="M1.5 6h9a4.5 4.5 0 0 1-9 0z" fill="#222"/><circle cx="6" cy="4" r="1.3" fill="#222"/></svg></div>
  <div class="feature" style="left:490px;top:164px;width:50px">Meals</div>
  <div class="icon" style="left:576px;top:128px"><svg viewBox="0 0 12 12"><circle cx="5" cy="2.6" r="1.5" fill="#222"/><rect x="3.5" y="4.5" width="3" height="6" fill="#222"/><path d="M8.5 2v8.5" stroke="#222" stroke-width="1"/></svg></div>
  <div class="feature" style="left:555px;top:164px;width:66px">Housekeeping</div>

  <div class="contact" style="left:384px;top:202px"><svg viewBox="0 0 10 10"><path d="M2 1l2 2-1 1.3a6 6 0 0 0 2.7 2.7L7 6l2 2-1.2 1.5C4 9 1 6 .6 2.2z" fill="#222"/></svg>808-732-1958</div>
  <div class="contact" style="left:384px;top:216px"><svg viewBox="0 0 10 10"><circle cx="5" cy="5" r="4.3" fill="none" stroke="#222" stroke-width="1"/><path d="M.7 5h8.6M5 .7c-2.4 2.6-2.4 6 0 8.6M5 .7c2.4 2.6 2.4 6 0 8.6" stroke="#222" stroke-width=".8" fill="none"/></svg>www.BrennerCare.com</div>
  <svg class="pin" style="left:490px;top:213px" viewBox="0 0 8 11"><path d="M4 0a4 4 0 0 1 4 4c0 3-4 7-4 7S0 7 0 4a4 4 0 0 1 4-4z" fill="#222"/><circle cx="4" cy="4" r="1.5" fill="#fff"/></svg>
  <div class="address" style="left:506px;top:202px">4870 Makani Ave.<br>Suite 310 Honolulu,<br>HI 96817</div>
  <div class="qr-space" style="left:600px;top:199px" role="img" aria-label="Space for QR code"></div>
</section>

<section class="card card--homecare">
  <div class="photo-main photo-main--homecare" role="img" aria-label="Photo of a nurse talking with a smiling senior man"></div>
  <svg class="shape" viewBox="0 0 640 240" aria-hidden="true">
    <path class="arc" d="M0 72 C60 40 135 75 157 150 C200 95 305 105 342 242 L0 242 Z"/>
    <rect class="cover" x="360" y="0" width="280" height="240"/>
  </svg>
  <div class="thumb" style="left:294px;top:18px;width:58px;height:58px;background:radial-gradient(circle,#b5c4bf,#6e857f)" role="img" aria-label="Photo of a home interior"></div>
  <div class="thumb" style="left:318px;top:50px;width:58px;height:58px;background:radial-gradient(circle,#cfded8,#7d9a90)" role="img" aria-label="Photo of seniors enjoying an activity together"></div>

  <div class="logo" style="left:9px;top:8px">
    <span class="logo-mark"></span><span class="logo-name">Brenner</span>
  </div>

  <div class="abs heading-light" style="left:10px;top:105px">HOMECARE</div>
  <div class="abs heading-bold" style="left:11px;top:126px">SERVICES:</div>

  <div class="icon" style="left:12px;top:167px"><svg viewBox="0 0 12 12"><circle cx="4" cy="4" r="1.6" fill="#222"/><circle cx="8" cy="4" r="1.6" fill="#222"/><rect x="2.5" y="6.5" width="7" height="3.5" rx="1" fill="#222"/></svg></div>
  <div class="abs label" style="left:51px;top:170px">Medication<br>Management</div>
  <div class="icon" style="left:12px;top:202px"><svg viewBox="0 0 12 12"><circle cx="6" cy="3.5" r="2.2" fill="#222"/><path d="M1.5 11a4.5 4.5 0 0 1 9 0z" fill="#222"/></svg></div>
  <div class="abs label" style="left:51px;top:210px">Skilled Nursing</div>

  <div class="divider" style="left:137px;top:170px;height:57px"></div>

  <div class="icon" style="left:165px;top:167px"><svg viewBox="0 0 12 12"><circle cx="4" cy="4" r="1.8" fill="#222"/><circle cx="8.5" cy="5" r="1.5" fill="#222"/><path d="M2 10a2.5 2.5 0 0 1 5 0zM6.5 10a2 2 0 0 1 4 0z" fill="#222"/></svg></div>
  <div class="abs label" style="left:200px;top:175px">Home Health Aides</div>
  <div class="icon" style="left:165px;top:202px"><svg viewBox="0 0 12 12"><path d="M1.5 5.5h9v2a3 3 0 0 1-3 3h-3a3 3 0 0 1-3-3z" fill="#222"/><path d="M3 5.5V3a1.3 1.3 0 0 1 2.6 0" stroke="#222" fill="none"/></svg></div>
  <div class="abs label" style="left:198px;top:210px">Bath &amp; Meal Service</div>

  <div class="abs heading-bold" style="left:389px;top:13px;font-size:21px;line-height:22px">INFORMATION</div>
  <p class="abs body-copy" style="left:389px;top:39px;width:241px">Brenner Care Group has been providing homecare to Oahu's Kupuna for the past 26 years. Brenner Homecare offers personal care services to meet your loved one's needs in the comfort and safety of their own home.</p>
  <p class="abs target" style="left:389px;top:88px;width:232px">Ages 55-105 Males and Females, looking for care or a home for themselves or their loved</p>
  <span class="abs" style="left:389px;top:118px;width:8px;height:8px;border-radius:50%;background:var(--accent)"></span>
  <div class="abs label--bold" style="left:407px;top:117px">Complimentary Care Consultation</div>

  <div class="panel" style="left:387px;top:141px;width:253px;height:43px;border-radius:22px 0 0 22px"></div>
  <div class="band-item" style="left:395px;top:153px">25+ Years in<br>business</div>
  <div class="band-divider" style="left:461px"></div>
  <div class="band-item" style="left:470px;top:153px">Locally owned<br>and operated</div>
  <div class="band-divider" style="left:540px"></div>
  <div class="band-item" style="left:550px;top:153px">Licensed and<br>Insured</div>

  <div class="contact" style="left:389px;top:200px"><svg viewBox="0 0 10 10"><path d="M2 1l2 2-1 1.3a6 6 0 0 0 2.7 2.7L7 6l2 2-1.2 1.5C4 9 1 6 .6 2.2z" fill="#222"/></svg>808-732-1958</div>
  <div class="contact" style="left:389px;top:213px"><svg viewBox="0 0 10 10"><circle cx="5" cy="5" r="4.3" fill="none" stroke="#222" stroke-width="1"/><path d="M.7 5h8.6M5 .7c-2.4 2.6-2.4 6 0 8.6M5 .7c2.4 2.6 2.4 6 0 8.6" stroke="#222" stroke-width=".8" fill="none"/></svg>www.BrennerCare.com</div>
  <svg class="pin" style="left:493px;top:208px" viewBox="0 0 8 11"><path d="M4 0a4 4 0 0 1 4 4c0 3-4 7-4 7S0 7 0 4a4 4 0 0 1 4-4z" fill="#222"/><circle cx="4" cy="4" r="1.5" fill="#fff"/></svg>
  <div class="address" style="left:509px;top:199px">4870 Makani Ave.<br>Suite 310 Honolulu,<br>HI 96817</div>
  <div class="qr-space" style="left:600px;top:198px" role="img" aria-label="Space for QR code"></div>
</section>

</body>
</html>
```